Nightclub-type Event Poster Advertisement

Lumora Events is based in Christchurch, New Zealand and we have our next party coming up. We like a different flair for each of our events so are looking for some help from you guys. We are very flexible with everything - colours, layout, backgrounds, fonts, etc so it's ALL up to you. Attached is our company logo and the flyer (and poster) we used for our last party. Our website is lumoranz.example where you can find and use our photos and find more info about us if you desire.
Designs we are wanting: An A3 poster,an A6 flyer (smaller version of the poster is probably fine), tickets (140x68 mm). It would be great if a 5 mm bleed was included so we could get them printed directly.
Details for the event to be advertised are as followed:
Party Name: (TBD... will update ASAP)
05/07/2014
10pm-close
Lineup: 'Vormp (Akl)', 'DJ Blunkett', 'DJ's Margosen & Pelwhit', 'Nine Paper Owls'.
Harlow Dunkers Hall, Corner Fennick & Oslow Streets
$10 Tickets
R18
Tickets & Enquiries: Tamsin on 0279041736
Presented by Lumora Entertainment
Thanks to everyone who reads this and please give it a go! Any questions don't hesitate to ask.
Target Market(s)
New Zealand Europeans in Christchurch, New Zealand between 18 and 25 years old.
Industry/Entity Type
Events
Look and feel

```html
<!DOCTYPE html>
<html lang="en">
<head>
<meta charset="utf-8">
<title>Lumora Entertainment – Event Poster</title>
<link href="https://fonts.googleapis.com/css2?family=Parisienne&family=Shadows+Into+Light&family=Playfair+Display:wght@700&display=swap" rel="stylesheet">
<style>
  :root {
    --page: #ffffff;
    --night-top: #2a0606;
    --night-mid: #120202;
    --night-bottom: #000000;
    --neon-yellow: #fff36a;
    --neon-red: #ff1a00;
    --neon-pink: #ff4fd8;
    --neon-magenta: #c02cff;
    --neon-orange: #ff6a00;
    --neon-blue: #1e3cff;
    --neon-violet: #8a2cff;
    --date-red: #c80000;
    --chevron: #8a0c0c;
    --white: #ffffff;
  }
  * { margin: 0; padding: 0; box-sizing: border-box; }
  html, body { width: 848px; height: 1200px; overflow: hidden; background: var(--page); }
  .poster {
    position: absolute; left: 14px; top: 14px; width: 820px; height: 1172px;
    background: linear-gradient(180deg, var(--night-top) 0%, var(--night-mid) 45%, var(--night-bottom) 75%);
    overflow: hidden;
    font-family: "Shadows Into Light", cursive;
    color: var(--white);
    text-transform: uppercase;
  }
  .presenter, .presents, .event-name, .lineup li, .details, .venue, .contact, .side-mark { position: absolute; }
  .presenter {
    top: 18px; width: 100%; text-align: center;
    font-family: "Parisienne", cursive; text-transform: none;
    font-size: 66px; line-height: 90px; color: var(--neon-yellow);
    text-shadow: 0 0 6px var(--neon-red), 0 0 14px var(--neon-red), 0 0 26px var(--neon-red);
  }
  .presents {
    top: 136px; width: 100%; text-align: center; text-transform: none;
    font-size: 22px; color: var(--neon-yellow);
    text-shadow: 0 0 6px var(--neon-red), 0 0 12px var(--neon-red);
  }
  .event-name {
    top: 206px; width: 100%; text-align: center;
    font-size: 76px; line-height: 100px; letter-spacing: 3px; color: #ffd6f6;
    text-shadow: 0 0 6px var(--neon-pink), 0 0 16px var(--neon-pink), 0 0 28px var(--neon-magenta);
  }
  .lineup { list-style: none; }
  .lineup li {
    width: 100%; text-align: center;
    font-size: 30px; letter-spacing: 1px; color: #fff0f0;
    text-shadow: 0 0 5px var(--neon-red), 0 0 12px var(--neon-red), 0 0 22px var(--neon-red);
  }
  .side-mark {
    top: 400px; width: 120px; text-align: center; text-transform: none;
    font-size: 26px; color: var(--neon-magenta);
  }
  .side-mark.left { left: 50px; }
  .side-mark.right { right: 50px; }
  .chevrons { position: absolute; left: 0; top: 562px; }
  .date {
    position: absolute; top: 560px; width: 100%; text-align: center;
    font-family: "Playfair Display", serif; font-weight: 700;
    font-size: 44px; line-height: 64px; letter-spacing: 10px; color: var(--date-red);
    text-transform: none;
  }
  .details { left: 16px; top: 650px; }
  .details p, .venue p { font-size: 40px; line-height: 78px; }
  .details p { color: #ffe0c0; text-shadow: 0 0 6px var(--neon-orange), 0 0 16px var(--neon-orange), 0 0 26px var(--neon-red); }
  .details .age { font-size: 30px; line-height: 60px; }
  .venue { right: 22px; top: 656px; text-align: right; }
  .venue p {
    font-size: 32px; line-height: 62px; color: #dfe6ff;
    text-shadow: 0 0 6px var(--neon-blue), 0 0 14px var(--neon-blue), 0 0 24px var(--neon-blue);
  }
  .dj-photo {
    position: absolute; left: 250px; top: 636px; width: 270px; height: 360px;
    background: radial-gradient(ellipse at 55% 40%, #8a5a3a 0%, #4a2a1a 35%, #1a0c06 65%, transparent 80%);
  }
  .contact {
    left: 26px; top: 1000px; width: 780px;
    font-size: 40px; line-height: 60px; color: #f0e0ff; white-space: nowrap;
    text-shadow: 0 0 6px var(--neon-violet), 0 0 16px var(--neon-violet), 0 0 26px var(--neon-violet);
  }
  .decks-photo {
    position: absolute; left: 0; bottom: 0; width: 820px; height: 100px;
    background: linear-gradient(180deg, #0c0c10 0%, #2a2a30 40%, #141418 100%);
  }
</style>
</head>
<body>
<main class="poster">
  <h2 class="presenter">Lumora Entertainment</h2>
  <p class="presents">presents</p>
  <h1 class="event-name">Event Name</h1>

  <ul class="lineup">
    <li style="top:322px">Vormp (Akl)</li>
    <li style="top:378px">DJ Blunkett</li>
    <li style="top:434px">DJ's Margosen &amp; Pelwhit</li>
    <li style="top:490px">Nine Paper Owls</li>
  </ul>

  <span class="side-mark left">Lumora</span>
  <span class="side-mark right">Lumora</span>

  <svg class="chevrons" width="820" height="60" viewBox="0 0 820 60" aria-hidden="true">
    <g fill="none" stroke="var(--chevron)" stroke-width="6">
      <path d="M-10 8 L12 30 L-10 52"/>
      <path d="M66 8 L90 30 L66 52"/>
      <path d="M146 8 L172 30 L146 52"/>
      <path d="M830 8 L808 30 L830 52"/>
      <path d="M754 8 L730 30 L754 52"/>
      <path d="M674 8 L648 30 L674 52"/>
    </g>
  </svg>
  <p class="date">05/07/2014</p>

  <div class="dj-photo" role="img" aria-label="Photo of a DJ in a cap and jacket dancing under warm light"></div>

  <div class="details">
    <p class="age">R 18</p>
    <p>10 pm – close</p>
    <p>$10 Tickets</p>
  </div>

  <div class="venue">
    <p>Harlow Dunkers Hall</p>
    <p>Corner Fennick &amp;</p>
    <p>Oslow Streets</p>
  </div>

  <p class="contact">Tickets &amp; Enquiries: Tamsin on 0279041736</p>

  <div class="decks-photo" role="img" aria-label="Photo of DJ turntables and mixer with glowing lights"></div>
</main>
</body>
</html>
```